STOREFRONT LIT SIGN for The Ranchera Loft

A sign advertising our music academy. This sign will be hung 10 feet above the entrance of our building and will be seen by all pedestrian and vehicle traffic on Birch Lane Delano.

Target Market(s)

Street passerby

Industry/Entity Type

Music Training

Font styles to use
Other font styles liked:
• Creative

Colors

Designer to choose colors to be used in the design.

Requirements
Must have
• A White Background
• Dimensions: 8 ft long x 3 ft tall
• The Ranchera Loft of Delano
• Lecciones de Piano, Violin, Guitarra, Voz, Trompeta y Mas
• MUSIC ACADEMY *(This should be most prominent)
• Guitar, Voice, Trumpet and More
• (661) 555-0147
• therancheraloft.example
Nice to have
• Graphics of a piano, or guitar, or violin or trumpet or a combination of two or more

```html
<!DOCTYPE html>
<html lang="es">
<head>
<meta charset="utf-8">
<title>The Ranchera Loft of Delano – Music Academy Sign</title>
<link rel="stylesheet" href="https://fonts.googleapis.com/css2?family=Patrick+Hand&family=Nunito:wght@800&display=swap">
<style>
  :root {
    --sign-white: #ffffff;
    --sign-red: #ec1c24;
    --ink: #111111;
  }
  html, body {
    margin: 0;
    padding: 0;
    overflow: hidden;
    background: var(--sign-white);
  }
  .sign {
    position: relative;
    width: 1200px;
    height: 452px;
    background: var(--sign-white);
    overflow: hidden;
    color: var(--ink);
    font-family: "Patrick Hand", cursive;
  }
  .sign__name {
    position: absolute;
    top: 26px;
    left: 0;
    width: 100%;
    margin: 0;
    text-align: center;
    font-size: 58px;
    font-weight: 400;
    line-height: 1;
  }
  .sign__lessons {
    position: absolute;
    top: 118px;
    left: 0;
    width: 100%;
    margin: 0;
    text-align: center;
    font-size: 34px;
    line-height: 1;
  }
  .band {
    position: absolute;
    left: 0;
    top: 178px;
    width: 1200px;
    height: 128px;
  }
  .band__shape { fill: var(--sign-red); }
  .band__title {
    position: absolute;
    left: 80px;
    top: 196px;
    margin: 0;
    color: var(--sign-white);
    font-size: 78px;
    font-weight: 400;
    letter-spacing: 2px;
    line-height: 1.2;
  }
  .band__divider {
    position: absolute;
    left: 730px;
    top: 210px;
    width: 7px;
    height: 68px;
    border-radius: 4px;
    background: var(--sign-white);
  }
  .instrument {
    position: absolute;
    top: 212px;
    height: 70px;
    border-radius: 8px;
    background: var(--sign-white);
  }
  .instrument--piano   { left: 782px;  width: 60px; }
  .instrument--guitar  { left: 908px;  width: 78px; }
  .instrument--trumpet { left: 1038px; width: 88px; }
  .sign__offer {
    position: absolute;
    left: 70px;
    top: 332px;
    margin: 0;
    font-size: 32px;
    line-height: 1.35;
  }
  .contact {
    position: absolute;
    right: 54px;
    top: 326px;
    text-align: right;
    font-family: "Nunito", sans-serif;
    font-weight: 800;
  }
  .contact__phone {
    display: block;
    font-size: 46px;
    line-height: 1.1;
    letter-spacing: 1px;
  }
  .contact__web {
    display: block;
    font-size: 33px;
    line-height: 1.3;
  }
</style>
</head>
<body>
  <main class="sign">
    <h1 class="sign__name">The Ranchera Loft of Delano</h1>
    <p class="sign__lessons">Lecciones de Piano, Violin, Guitarra, Voz, Trompeta y Mas</p>

    <svg class="band" viewBox="0 0 1200 128" aria-hidden="true">
      <path class="band__shape" d="M0 6 L120 2 L260 7 L420 1 L560 6 L720 2 L860 7 L1000 2 L1120 6 L1200 3 L1200 124 L1080 128 L940 121 L800 126 L640 120 L480 125 L330 121 L180 127 L60 122 L0 125 Z"/>
    </svg>
    <h2 class="band__title">MUSIC ACADEMY</h2>
    <span class="band__divider"></span>
    <span class="instrument instrument--piano" role="img" aria-label="Piano keyboard graphic"></span>
    <span class="instrument instrument--guitar" role="img" aria-label="Acoustic guitar graphic"></span>
    <span class="instrument instrument--trumpet" role="img" aria-label="Trumpet graphic"></span>

    <p class="sign__offer">Guitar, Voice,<br>Trumpet and More</p>
    <address class="contact">
      <span class="contact__phone">(661) 555-0147</span>
      <span class="contact__web">therancheraloft.example</span>
    </address>
  </main>
</body>
</html>
```